property investment and development company needs a website

we need a website that looks professional and portrays trust for people looking to us to buy their house or investors looking to invest or joint venture with us.
We are based in the west midlands in the UK.
we deal mainly with residential housing, house to flats conversions, HMO's (houses in multiple ocupancy).
we require the website as a first point of contact with potential sellers, renters and investors so links or contact details that are easy to access or see would be good.
I have had logos designed by a plan hollow member and these can be used as guidance for the colour and style of the site.
Target Market(s)
joint venture investment partners, people looking to sell their house, people looking to rent from us.
Coding
Coded - Design and coding required
Number of Pages Required
3 page
Requirements
Must have
- project a professional appearance
- visable contact details

```html
<!DOCTYPE html>
<html lang="en">
<head>
<meta charset="utf-8">
<title>Ashford Homes — Property Investment &amp; Development</title>
<link href="https://fonts.googleapis.com/css2?family=Cinzel:wght@400;700&family=Lato:wght@400;700&family=Libre+Baskerville&display=swap" rel="stylesheet">
<style>
:root{
  --gold:#c7a86c;
  --gold-dark:#b39357;
  --ink:#2f2f2f;
  --charcoal:#3b3b3d;
  --page:#efefef;
  --white:#ffffff;
  --muted:#6b6b6b;
  --accent:#e0604f;
  --cyan:#2ec6e6;
  --badge-sell:#a5c23b;
  --badge-buy:#3cb0e2;
  --badge-rent:#e8336d;
  --footer:#2a2a2b;
  --footer-bar:#222223;
}
*{box-sizing:border-box;margin:0;padding:0}
html,body{width:1200px;height:3267px;overflow:hidden}
body{background:var(--page);font-family:'Lato',sans-serif;color:var(--ink);position:relative}
.abs{position:absolute}
a{color:inherit;text-decoration:none}

/* top bar */
.topbar{left:0;top:0;width:1200px;height:55px;background:var(--page);border-bottom:1px solid #dcdcdc}
.topbar .phone{left:120px;top:18px;font-size:12px;display:flex;align-items:center;gap:10px}
.social-top{left:620px;top:10px;display:flex}
.social-top span{width:36px;height:36px;border-left:1px solid #d4d4d4;display:flex;align-items:center;justify-content:center}
.social-top span:last-child{border-right:1px solid #d4d4d4}
.social-top i{width:14px;height:14px;border:2px solid var(--ink);display:block}
.lang{left:864px;top:16px;font-size:10px;display:flex;align-items:center;gap:10px}
.lang b{width:28px;height:18px;background:#2b4aa0;display:block}
.login{left:961px;top:11px;width:120px;height:32px;background:var(--gold);color:var(--white);font-size:10px;display:flex;align-items:center;justify-content:center;border-radius:2px}

/* nav */
.nav{left:0;top:55px;width:1200px;height:85px;background:var(--page)}
.brand{left:120px;top:24px;display:flex;align-items:center;gap:12px}
.brand i{width:36px;height:36px;background:var(--gold);display:block}
.brand span{font-family:'Cinzel',serif;font-size:21px;line-height:22px;color:var(--charcoal);letter-spacing:1px}
.menu{right:120px;top:36px;display:flex;gap:42px;font-size:12px}
.menu .current{color:var(--accent)}

/* hero */
.hero{left:0;top:140px;width:1200px;height:575px;background:linear-gradient(120deg,#7a6a5c 0%,#9b8a7b 35%,#5f5a58 60%,#b9b4ae 100%)}
.hero h1{left:0;top:222px;width:1200px;text-align:center;font-family:'Cinzel',serif;font-weight:400;font-size:38px;color:var(--white);letter-spacing:1px}
.hero p{left:0;top:276px;width:1200px;text-align:center;font-size:19px;color:var(--white);letter-spacing:1px}
.search{left:245px;top:317px;display:flex;gap:10px}
.field{height:38px;background:var(--white);font-size:11px;color:var(--muted);display:flex;align-items:center;padding:0 10px;gap:8px;border-radius:2px}
.field.select{justify-content:space-between;color:var(--ink)}
.btn-search{width:160px;height:38px;background:var(--gold);color:var(--white);font-size:11px;display:flex;align-items:center;justify-content:center;border-radius:2px}

/* section heading */
.sec-head{left:0;width:1200px;text-align:center;font-family:'Cinzel',serif;font-size:19px;line-height:21px;color:var(--ink)}
.sec-head em{font-style:normal;color:var(--gold)}

/* about */
.about-frame{left:120px;top:937px;width:479px;height:396px;border:3px solid var(--ink)}
.about-photo{left:157px;top:904px;width:479px;height:398px;background:linear-gradient(180deg,#6fb0e6 0%,#b9dcf0 40%,#a7794a 55%,#2ec0c8 80%,#16a5b0 100%)}
.about-text{left:721px;top:976px;width:352px;font-family:'Libre Baskerville',serif;font-size:12px;line-height:23.5px;color:var(--ink);text-align:justify}
.btn-dark{background:var(--charcoal);color:var(--white);font-size:10px;display:flex;align-items:center;justify-content:center;border-radius:2px;letter-spacing:.5px}

/* featured */
.feat-bar{left:120px;top:1400px;width:960px;height:96px;background:var(--charcoal)}
.arrow-btn{width:38px;height:38px;display:flex;align-items:center;justify-content:center;border-radius:2px}
.feat-title{left:0;top:27px;width:960px;text-align:center;font-family:'Cinzel',serif;font-size:19px;line-height:22px;color:var(--white)}
.feat-title em{font-style:normal;color:var(--gold)}
.view-all{right:14px;top:30px;width:80px;height:36px;background:var(--gold);color:var(--white);font-size:10px;display:flex;align-items:center;justify-content:center;border-radius:2px}
.card{top:1529px;width:305px;height:240px}
.card .photo{left:0;top:0;width:305px;height:240px}
.card .badge{right:28px;top:18px;width:56px;height:28px;color:var(--white);font-size:10px;display:flex;align-items:center;justify-content:center}
.card h3{left:22px;top:148px;font-family:'Libre Baskerville',serif;font-weight:400;font-size:14px;color:var(--white)}
.card small{left:22px;top:170px;font-size:9px;color:#eee}
.card .price{left:18px;top:202px;width:62px;height:24px;background:var(--gold);color:var(--white);font-size:11px;display:flex;align-items:center;justify-content:center}
.card .tools{right:14px;top:206px;display:flex;gap:10px}
.card .tools i{width:14px;height:14px;border:1.5px solid var(--white);display:block;border-radius:2px}

/* book band */
.book{left:0;top:1830px;width:1200px;height:240px;background:linear-gradient(180deg,#1f1b2e 0%,#2c2140 55%,#1a1626 100%)}
.book-box{left:355px;top:60px;width:479px;height:114px;border:1px solid rgba(255,255,255,.6);text-align:center}
.book-box h2{margin-top:30px;font-size:23px;font-weight:400;color:var(--white);letter-spacing:1px}
.book-box p{margin-top:6px;font-size:14px;color:var(--cyan);letter-spacing:1px}

/* testimonials */
.testi{left:120px;top:2239px;width:963px;height:322px;background:var(--white);box-shadow:0 2px 6px rgba(0,0,0,.08)}
.testi .gold{left:0;top:0;width:283px;height:322px;background:var(--gold)}
.testi .person{left:133px;top:48px;width:231px;height:233px;background:linear-gradient(180deg,#d9d6d0 0%,#f2f2f2 60%,#c9c4bc 100%);border:3px solid var(--white)}
.testi .name{left:426px;top:50px;font-size:14px}
.testi .role{left:426px;top:70px;font-size:11px;color:var(--muted)}
.testi .quote{left:442px;top:111px;width:440px;font-size:11px;line-height:24px;color:var(--muted)}
.circle{width:48px;height:48px;border-radius:50%;background:var(--charcoal);display:flex;align-items:center;justify-content:center}

/* split band */
.split{left:0;top:2620px;width:1200px;height:288px}
.split h3{font-size:17px;font-weight:400;color:var(--white)}
.split p{font-size:11.5px;line-height:20px;color:#e6e6e6}

/* footer */
.footer{left:0;top:2908px;width:1200px;height:287px;background:var(--footer)}
.footer h4{font-size:13px;font-weight:700;color:var(--white)}
.footer ul{list-style:none;font-size:11px;color:#ddd;line-height:29px}
.footer .gold-text{color:var(--gold)}
.fcol{top:78px}
.recent{display:flex;gap:14px;align-items:center;margin-top:12px}
.recent i{width:48px;height:40px;background:linear-gradient(135deg,#7c8a95,#c4c8c9);display:block}
.recent div{font-size:11px;color:#ddd;line-height:21px}
.f-social{display:flex;gap:12px;margin-top:14px}
.f-social i{width:18px;height:18px;border:2px solid #ddd;display:block}
.f-brand{display:flex;align-items:center;gap:10px}
.f-brand i{width:32px;height:32px;background:var(--gold);display:block}
.f-brand span{font-family:'Cinzel',serif;font-size:18px;line-height:19px;color:var(--white);letter-spacing:1px}
.copyright{left:0;top:3195px;width:1200px;height:72px;background:var(--footer-bar);border-top:1px solid #3a3a3a;color:#bbb;font-size:11px;display:flex;align-items:center;justify-content:center}
</style>
</head>
<body>

<header>
  <div class="abs topbar">
    <div class="abs phone">
      <svg width="10" height="16" viewBox="0 0 10 16"><rect x="1" y="1" width="8" height="14" rx="1.5" fill="none" stroke="#2f2f2f" stroke-width="1.5"/><circle cx="5" cy="12.5" r=".9" fill="#2f2f2f"/></svg>
      0-700-2 48-5521
    </div>
    <div class="abs social-top"><span><i></i></span><span><i></i></span><span><i></i></span><span><i></i></span></div>
    <div class="abs lang"><b role="img" aria-label="Language flag"></b>English</div>
    <a class="abs login" href="#">&#9678;&nbsp; Login/Register</a>
  </div>

  <div class="abs nav">
    <div class="abs brand"><i></i><span>ASHFORD<br>HOMES</span></div>
    <nav class="abs menu">
      <a class="current" href="#">Home</a><a href="#">About Us</a><a href="#">Invest</a><a href="#">Sell</a><a href="#">Contact Us</a>
    </nav>
  </div>
</header>

<section class="abs hero" role="img" aria-label="Photo of a young couple meeting an estate agent with a small model house on the table">
  <h1 class="abs">FIND YOUR NEW HOME</h1>
  <p class="abs">ITS JUST A FEW CLICKS AWAY.</p>
  <form class="abs search">
    <div class="field" style="width:240px">
      <svg width="12" height="12" viewBox="0 0 12 12"><circle cx="5" cy="5" r="3.8" fill="none" stroke="#555" stroke-width="1.4"/><line x1="8" y1="8" x2="11" y2="11" stroke="#555" stroke-width="1.4"/></svg>
      Street, City, State, Zip or keyword
    </div>
    <div class="field select" style="width:140px">All Cities <span>&#9662;</span></div>
    <div class="field select" style="width:140px">All States <span>&#9662;</span></div>
    <div class="btn-search">SEARCH</div>
  </form>
</section>

<h2 class="abs sec-head" style="top:776px">ABOUT<br><em>ASHFORD HOMES</em></h2>

<section>
  <div class="abs about-frame"></div>
  <div class="abs about-photo" role="img" aria-label="Photo of a luxury overwater villa with a thatched roof, deck and boat on turquoise water"></div>
  <p class="abs about-text">We are a property development and investment company that have our own portfolio and we are active investors who pride ourselves in expanding our business organically. We ensure that whatever your property needs are we deliver bespoke services for our clients. For investors, sellers, landlords and tenants we bring knowledge to your next property decision, allowing you to make an informed decision.</p>
  <a class="abs btn-dark" href="#" style="left:721px;top:1187px;width:120px;height:37px">LEARN MORE</a>
</section>

<section>
  <div class="abs feat-bar">
    <div class="abs arrow-btn" style="left:18px;top:29px;background:var(--gold)"><svg width="8" height="12" viewBox="0 0 8 12"><path d="M6 1L1 6l5 5" fill="none" stroke="#fff" stroke-width="1.6"/></svg></div>
    <div class="abs arrow-btn" style="left:62px;top:29px;background:#555"><svg width="8" height="12" viewBox="0 0 8 12"><path d="M2 1l5 5-5 5" fill="none" stroke="#fff" stroke-width="1.6"/></svg></div>
    <h2 class="abs feat-title">FEATURED<br><em>RESIDENTIAL HOUSING</em></h2>
    <a class="abs view-all" href="#">View All &#8250;</a>
  </div>

  <article class="abs card" style="left:122px">
    <div class="abs photo" role="img" aria-label="Photo of a modern glass villa with a lit pool at dusk" style="background:linear-gradient(180deg,#3a4a7a 0%,#6b5a80 40%,#c48a4a 70%,#2a3a5a 100%)"></div>
    <span class="abs badge" style="background:var(--badge-sell)">SELL</span>
    <h3 class="abs">Harbour Loft</h3>
    <small class="abs">Bay Road, Harbourside, UK</small>
    <span class="abs price">$ 2000</span>
    <div class="abs tools"><i></i><i></i><i></i><i></i></div>
  </article>
  <article class="abs card" style="left:448px">
    <div class="abs photo" role="img" aria-label="Photo of a hillside villa above a city at sunset" style="background:linear-gradient(180deg,#7a5a4a 0%,#b07050 40%,#6a4a3a 70%,#3a2e2a 100%)"></div>
    <span class="abs badge" style="background:var(--badge-buy)">BY</span>
    <h3 class="abs">Villa Serena</h3>
    <small class="abs">Hill Lane, Westvale, UK</small>
    <span class="abs price">$ 4000</span>
    <div class="abs tools"><i></i><i></i><i></i><i></i></div>
  </article>
  <article class="abs card" style="left:775px">
    <div class="abs photo" role="img" aria-label="Photo of a contemporary white house with a swimming pool" style="background:linear-gradient(180deg,#8aa0b4 0%,#c8ccd0 45%,#6a7a80 70%,#3a4a50 100%)"></div>
    <span class="abs badge" style="background:var(--badge-rent)">RENT</span>
    <h3 class="abs">The Willows</h3>
    <small class="abs">Mill Road, Eastbrook, UK</small>
    <span class="abs price">$ 5000</span>
    <div class="abs tools"><i></i><i></i><i></i><i></i></div>
  </article>
</section>

<section class="abs book" role="img" aria-label="Night city skyline in deep purple tones">
  <div class="abs book-box">
    <h2>BOOK YOUR PROPERTY</h2>
    <p>CALL US ON: 0-150-3 62-4407</p>
  </div>
</section>

<h2 class="abs sec-head" style="top:2146px">TESTIMONIALS</h2>

<section>
  <div class="abs testi">
    <div class="abs gold" role="img" aria-label="Gold panel with faint hexagon pattern"></div>
    <div class="abs person" role="img" aria-label="Portrait photo of the reviewing estate agent in a white polo shirt"></div>
    <div class="abs name">Tobin Reeve</div>
    <div class="abs role">Real Estate Agent</div>
    <p class="abs quote"><b style="font-size:18px;color:var(--ink)">&ldquo;</b> Sorem ipsum dolor sit amet, consectetur adipiscing elit. Sed tempor as, vel tincidunt ipsum posuere ut pellentesque sollicitudin duis iaculis, arcu ut velit. Sorem ipsum dolor sit amet, consectetur adipiscing elit. Sed tempor as, vel tincidunt ipsum posuere ut pellentesque sollicitudin duis iaculis, arcu ut velit. <b style="font-size:18px;color:var(--ink)">&rdquo;</b></p>
  </div>
  <div class="abs circle" style="left:97px;top:2378px"><svg width="10" height="14" viewBox="0 0 10 14"><path d="M8 1L2 7l6 6" fill="none" stroke="#fff" stroke-width="2"/></svg></div>
  <div class="abs circle" style="left:1058px;top:2378px"><svg width="10" height="14" viewBox="0 0 10 14"><path d="M2 1l6 6-6 6" fill="none" stroke="#fff" stroke-width="2"/></svg></div>
</section>

<section class="abs split">
  <svg class="abs" style="left:0;top:0" width="1200" height="288" viewBox="0 0 1200 288" role="img" aria-label="Dusk photo of a large house, split into charcoal and gold tinted halves">
    <polygon points="0,0 640,0 555,288 0,288" fill="#3a3836"/>
    <polygon points="640,0 1200,0 1200,288 555,288" fill="#b39a68"/>
  </svg>
  <div class="abs" style="left:120px;top:72px;width:480px">
    <h3>PROPERTY INVESTORS</h3>
    <p style="margin-top:6px">We have our own portfolio and we are active investors, so our finger is on the pulse and we are currently looking for residential development investments &amp; commercial to residential conversions in cities or regional centres showing.</p>
    <a class="btn-dark" href="#" style="margin-top:14px;width:120px;height:37px;background:var(--gold)">LEARN MORE</a>
  </div>
  <div class="abs" style="left:654px;top:72px;width:430px">
    <h3>PROPERTY SALE</h3>
    <p style="margin-top:6px">We undertake the necessary market research to evaluate an option that works for all parties involved. We will help guide you to make an informed decision on to gain the maximum realistic value.</p>
    <a class="btn-dark" href="#" style="margin-top:14px;width:120px;height:37px">LEARN MORE</a>
  </div>
</section>

<footer>
  <div class="abs footer">
    <div class="abs fcol" style="left:120px">
      <h4>Quick Links</h4>
      <ul style="margin-top:6px"><li>Home</li><li>About Us</li><li>Invest</li><li>Sell</li><li>Contact Us</li></ul>
    </div>
    <div class="abs fcol" style="left:324px;width:220px">
      <h4>Contact Us</h4>
      <div style="display:flex;gap:12px;margin-top:14px">
        <svg width="12" height="16" viewBox="0 0 12 16"><path d="M6 15s5-5.5 5-9A5 5 0 0 0 1 6c0 3.5 5 9 5 9z" fill="none" stroke="#ddd" stroke-width="1.4"/><circle cx="6" cy="6" r="1.8" fill="#ddd"/></svg>
        <div class="gold-text" style="font-size:11.5px;line-height:19px">12 Larchfield Road,<br>Ledbury, Herefordshire,<br>HR8 2QT</div>
      </div>
      <div style="display:flex;gap:12px;margin-top:8px;font-size:11.5px" class="gold-text">
        <svg width="12" height="12" viewBox="0 0 12 12"><path d="M2 1l2.5 0 1 3-1.5 1a7 7 0 0 0 3 3l1-1.5 3 1V11A10 10 0 0 1 1 2z" fill="none" stroke="#ddd" stroke-width="1.2"/></svg>
        0-700-2 48-5521
      </div>
      <div style="display:flex;gap:12px;margin-top:12px;font-size:11.5px;color:#ddd">
        <svg width="13" height="10" viewBox="0 0 13 10"><rect x=".7" y=".7" width="11.6" height="8.6" fill="none" stroke="#ddd" stroke-width="1.2"/><path d="M1 1l5.5 4.5L12 1" fill="none" stroke="#ddd" stroke-width="1.2"/></svg>
        hello@ashfordhomes.example
      </div>
    </div>
    <div class="abs fcol" style="left:590px">
      <h4>Recent Properties</h4>
      <div class="recent"><i role="img" aria-label="Thumbnail of a house"></i><div>Elmstead Row<br>$10,000</div></div>
      <div class="recent"><i role="img" aria-label="Thumbnail of a house"></i><div>Birch Court<br>$20,000</div></div>
    </div>
    <div class="abs fcol" style="left:823px">
      <h4>Follow US</h4>
      <div class="f-social"><i></i><i></i><i></i><i></i></div>
      <div class="f-brand" style="margin-top:44px"><i></i><span>ASHFORD<br>HOMES</span></div>
    </div>
  </div>
  <div class="abs copyright">Copyright@ 2019, Ashford Homes &amp; Developments Ltd &nbsp;|&nbsp; 10485527</div>
</footer>

</body>
</html>
```